Storytelling podcast needs podcast artwork

We need a logo design for a new podcast called 'Across Still Waters, Walking Home Again'. The podcast will tell the story of family whose young daughter suddenly and expectedly goes blind. We would like to see designs that play on the concepts of shading, transition, and contrast. The final design communicate the challenges of being in darkness and the reward of finding light.

Requirements
Must have
• 1800 x 1800 pixel image. No text in bottom 1/4 of image.

```html
<!DOCTYPE html>
<html lang="en">
<head>
<meta charset="utf-8">
<title>Across Still Waters, Walking Home Again — Podcast Artwork</title>
<link rel="stylesheet" href="https://fonts.googleapis.com/css2?family=Josefin+Sans:wght@400;600;700&display=swap">
<style>
  :root {
    --ink: #161616;
    --frame: #e6d24a;
    --shadow-deep: #0b0b0b;
    --shadow-mid: #2c2c2c;
    --mist: #c9cdcd;
    --glow: #fbfbf4;
    --glow-warm: #f3eea0;
  }
  * { margin: 0; padding: 0; box-sizing: border-box; }
  html, body {
    width: 1200px;
    height: 1200px;
    overflow: hidden;
    background: var(--shadow-deep);
  }
  .artwork {
    position: relative;
    width: 1200px;
    height: 1200px;
    overflow: hidden;
    font-family: "Josefin Sans", sans-serif;
    color: var(--ink);
  }
  .scene {
    position: absolute;
    inset: 0;
    background:
      radial-gradient(ellipse 260px 180px at 880px 20px, var(--glow) 0%, var(--glow-warm) 45%, rgba(243,238,160,0) 100%),
      radial-gradient(ellipse 420px 620px at 640px 420px, rgba(245,245,242,0.95) 0%, rgba(200,204,204,0.75) 45%, rgba(60,62,62,0) 100%),
      radial-gradient(ellipse 520px 760px at 600px 560px, var(--mist) 0%, var(--shadow-mid) 60%, var(--shadow-deep) 100%);
  }
  .frame {
    position: absolute;
    left: 23px;
    top: 23px;
    width: 1154px;
    height: 1154px;
    border: 4px solid var(--frame);
    pointer-events: none;
  }
  .title {
    position: absolute;
    left: 0;
    width: 1200px;
    text-align: center;
    line-height: 1;
    white-space: nowrap;
  }
  .title--kicker {
    font-weight: 400;
    letter-spacing: 0.08em;
  }
  .title--main {
    font-weight: 700;
    letter-spacing: 0.12em;
    padding-left: 0.12em;
  }
  .title--line1 { top: 92px;  font-size: 62px; }
  .title--line2 { top: 160px; font-size: 168px; }
  .title--line3 { top: 344px; font-size: 46px; }
  .title--line4 { top: 400px; font-size: 188px; }
</style>
</head>
<body>
  <main class="artwork">
    <div class="scene" role="img" aria-label="Misty cave in grey tones with bright warm light streaming in from the upper right; a small silhouetted girl stands on a rocky peak below, reaching up toward a balloon floating into the light"></div>

    <h1 class="podcast-title">
      <span class="title title--kicker title--line1">ACROSS STILL</span>
      <span class="title title--main title--line2">WATERS</span>
      <span class="title title--kicker title--line3">WALKING HOME</span>
      <span class="title title--main title--line4">AGAIN</span>
    </h1>

    <div class="frame"></div>
  </main>
</body>
</html>
```